Real Estate Entrepreneur needs a business card

I am a real estate entrepreneur, I buy houses for investment purposes, I act as a real estate agent representing buyers and sellers in residential home transactions, I am a contractor that does a wide range of home repairs and construction. I'd like a design that can stick with me through the years as my business grows and morphs to fit any niche I decide to pursue as markets change.

Target Market(s)

Anyone with interest that may be related to real estate.

Industry/Entity Type

Real Estate

Contact Information for Business Card

A card that stands out and doesn't put me in any one box. My business will evolve over time and I need a card that can stay relevant.

Colors

Designer to choose colors to be used in the design.

Requirements
Must have
• Character
Nice to have
• I'm open
Should not have
• Cliche houses and hammers

```html
<!DOCTYPE html>
<html lang="en">
<head>
<meta charset="utf-8">
<title>Cole Barton – Business Card</title>
<link rel="stylesheet" href="https://fonts.googleapis.com/css2?family=Roboto+Slab:wght@700&family=Open+Sans:wght@600&family=Montserrat:wght@400&display=swap">
<style>
  :root {
    --navy: #12355f;
    --paper: #f7f7f5;
    --ink-grey: #5f5f5f;
    --rule-grey: #7a7a7a;
    --backdrop: #e4e6ea;
    --white: #ffffff;
  }
  * { box-sizing: border-box; margin: 0; padding: 0; }
  html, body { width: 1200px; height: 800px; overflow: hidden; }
  body {
    background: var(--backdrop);
    display: flex;
    align-items: center;
    justify-content: center;
    gap: 40px;
  }
  .card {
    position: relative;
    width: 540px;
    height: 309px;
    overflow: hidden;
    box-shadow: 0 10px 28px rgba(20, 30, 50, 0.18);
  }
  .card--front { background: var(--paper); }
  .card--back {
    background: var(--navy);
    display: flex;
    align-items: center;
    justify-content: center;
  }
  .brand-name {
    font-family: "Roboto Slab", serif;
    font-weight: 700;
    color: var(--white);
    font-size: 54px;
    letter-spacing: 1px;
  }
  .identity {
    position: absolute;
    left: 40px;
    top: 132px;
  }
  .identity__name {
    font-family: "Roboto Slab", serif;
    font-weight: 700;
    font-size: 28px;
    line-height: 1;
    color: var(--navy);
  }
  .identity__title {
    font-family: "Open Sans", sans-serif;
    font-weight: 600;
    font-size: 19px;
    line-height: 1.25;
    color: var(--ink-grey);
    margin-left: 4px;
  }
  .rule-accent {
    position: absolute;
    left: 44px;
    top: 190px;
    width: 226px;
    height: 3px;
    background: var(--navy);
  }
  .rule-line {
    position: absolute;
    left: 270px;
    top: 191px;
    width: 232px;
    height: 1px;
    background: var(--rule-grey);
  }
  .contact-list {
    position: absolute;
    left: 46px;
    top: 204px;
    list-style: none;
  }
  .contact-list li,
  .address {
    display: flex;
    align-items: center;
    gap: 6px;
    font-family: "Montserrat", sans-serif;
    font-size: 13px;
    line-height: 19px;
    color: var(--ink-grey);
  }
  .icon { width: 13px; height: 13px; flex: none; }
  .address {
    position: absolute;
    right: 38px;
    top: 204px;
  }
</style>
</head>
<body>
  <section class="card card--front" aria-label="Business card front">
    <div class="identity">
      <h1 class="identity__name">COLE BARTON</h1>
      <p class="identity__title">Owner/Manager</p>
    </div>
    <div class="rule-accent"></div>
    <div class="rule-line"></div>

    <ul class="contact-list">
      <li>
        <svg class="icon" viewBox="0 0 24 24" aria-hidden="true"><path fill="#12355f" d="M6.6 10.8a15.1 15.1 0 0 0 6.6 6.6l2.2-2.2c.3-.3.7-.4 1-.2 1.1.4 2.3.6 3.6.6.6 0 1 .4 1 1V20c0 .6-.4 1-1 1A17 17 0 0 1 3 4c0-.6.4-1 1-1h3.5c.6 0 1 .4 1 1 0 1.3.2 2.5.6 3.6.1.3 0 .7-.2 1z"/></svg>
        (555)2XX-7304
      </li>
      <li>
        <svg class="icon" viewBox="0 0 24 24" aria-hidden="true"><rect x="2" y="5" width="20" height="14" fill="none" stroke="#12355f" stroke-width="1.8"/><path d="M2 5l10 8 10-8M2 19l7-7M22 19l-7-7" fill="none" stroke="#12355f" stroke-width="1.5"/></svg>
        colebartonmail.com
      </li>
      <li>
        <svg class="icon" viewBox="0 0 24 24" aria-hidden="true"><rect x="2" y="5" width="20" height="14" fill="none" stroke="#12355f" stroke-width="1.8"/><path d="M2 5l10 8 10-8M2 19l7-7M22 19l-7-7" fill="none" stroke="#12355f" stroke-width="1.5"/></svg>
        info@colebartonweb.com
      </li>
      <li>
        <svg class="icon" viewBox="0 0 24 24" aria-hidden="true"><circle cx="12" cy="12" r="10" fill="#12355f"/><path d="M2 12h20M12 2c3 3 3 17 0 20M12 2c-3 3-3 17 0 20" fill="none" stroke="#f7f7f5" stroke-width="1.3"/></svg>
        www.colebartonweb.com
      </li>
    </ul>

    <p class="address">
      <svg class="icon" viewBox="0 0 24 24" aria-hidden="true"><path fill="#12355f" d="M12 2a7 7 0 0 0-7 7c0 5 7 13 7 13s7-8 7-13a7 7 0 0 0-7-7zm0 9.5A2.5 2.5 0 1 1 12 6.5a2.5 2.5 0 0 1 0 5z"/></svg>
      742 5th Avenue North
    </p>
  </section>

  <section class="card card--back" aria-label="Business card back">
    <p class="brand-name">COLE BARTON</p>
  </section>
</body>
</html>
```